Looking to build a senior life alert web page

We definitely want to incorporate pictures of the product in which we're selling and want colors that resonate with the senior community. We're looking for something also clean and very easy to navigate. We're looking to pick a design immediately!
Based on something similar to that of our competition which can be located at the following
https://www.corvenhelpline.com/
https://www.trellowatch.com/

attached is the product we're selling

The name of our company is the elder harbor circle

Target Market(s)

Elderly people looking for a life alert device

Industry/Entity Type

Medical Equipment

Number of Pages Required

3 page

Font styles to use
Serif

Colors

Designer to choose colors to be used in the design.

Requirements
Must have
• Pictures of the product a nice UI experience that can be easily made mobile friendly
Nice to have
• Including area for video content maybe / friendly color LOGOS are attached for our company

```html
<!DOCTYPE html>
<html lang="en">
<head>
<meta charset="utf-8">
<title>Elder Harbor Circle – Medical Alert Systems</title>
<link href="https://fonts.googleapis.com/css2?family=Alegreya+Sans:wght@300;400;500;700&family=Lato:wght@400;700&display=swap" rel="stylesheet">
<style>
:root{
  --accent:#e0482c;
  --navy:#123f74;
  --navy-deep:#0f3966;
  --ink:#2e3440;
  --muted:#6b7078;
  --line:#c9ccd2;
  --band:#eceef1;
  --footer:#e6e8ec;
  --bar:#4a4d54;
  --white:#ffffff;
}
*{box-sizing:border-box;margin:0;padding:0}
html,body{width:1200px;height:3727px;overflow:hidden}
body{position:relative;background:var(--white);font-family:"Lato",Arial,sans-serif;color:var(--ink)}
.abs{position:absolute}
h1,h2,h3,.heading{font-family:"Alegreya Sans","Trebuchet MS",sans-serif;font-weight:400}
.btn{position:absolute;display:flex;align-items:center;justify-content:center;border-radius:18px;font-family:"Lato",sans-serif;font-weight:700;font-size:13px;color:var(--white)}
.btn-accent{background:var(--accent)}
.btn-navy{background:var(--navy)}
.btn-ghost{border:2px solid var(--accent);color:var(--white)}
.rule{position:absolute;height:1px;background:var(--line)}
.lead{position:absolute;font-size:14px;line-height:22px;color:var(--muted)}
.dots{position:absolute;display:flex;gap:6px}
.dots i{width:6px;height:6px;border-radius:50%;background:#7a7f88;display:block}
.dots.light i{background:#c6d3e4}

/* header */
.site-header{position:absolute;left:0;top:0;width:1200px;height:112px;z-index:2}
.brand{position:absolute;left:150px;top:34px;display:flex;align-items:center;gap:10px}
.brand-dot{width:34px;height:34px;border-radius:50%;background:var(--accent)}
.brand-name{font-family:"Alegreya Sans",sans-serif;font-weight:700;font-size:19px;color:var(--navy)}
.call{position:absolute;left:724px;top:26px;font-size:17px;color:var(--navy)}
.call b{color:var(--accent);font-weight:400}
.login{left:930px;top:19px;width:113px;height:36px;font-size:14px}
.nav{position:absolute;left:400px;top:68px;display:flex;gap:38px;font-size:14px;color:var(--navy)}
.nav .active{color:var(--accent);position:relative}
.nav .active:after{content:"";position:absolute;left:-6px;right:-6px;bottom:-12px;height:2px;background:var(--accent)}

/* hero */
.hero{position:absolute;left:0;top:0;width:1200px;height:591px;background:linear-gradient(180deg,#f4f4f3 0%,#e9e9e7 55%,#d5d4d1 100%)}
.hero-kicker{left:154px;top:258px;font-size:18px;color:var(--accent);font-family:"Alegreya Sans",sans-serif}
.hero-title{left:154px;top:286px;font-size:40px;line-height:48px;color:var(--navy);font-weight:300}
.hero-cta{left:154px;top:410px;width:169px;height:33px}
.hero-product{left:520px;top:190px;width:557px;height:372px;border-radius:24px;background:linear-gradient(135deg,#ffffff 0%,#eceef0 60%,#d7dadd 100%)}

/* how it works */
.steps{position:absolute;left:305px;top:765px;display:flex;gap:0}
.step{width:220px;font-size:16px;line-height:22px;color:var(--ink)}
.step svg{display:block;margin-bottom:46px}

/* video + about */
.grey-band{left:0;top:1222px;width:1200px;height:500px;background:var(--band)}
.video{left:231px;top:1060px;width:738px;height:320px;background:linear-gradient(180deg,#b9cde0 0%,#8ea7b8 45%,#4d6a55 80%,#3b5542 100%)}
.play{left:566px;top:1187px}

/* products */
.card{position:absolute;top:1913px;width:224px;height:367px;border:2px solid #dadde2;background:var(--white)}
.card.featured{border-color:#eaa394}
.card-head{height:78px;background:#e6ecf4;display:flex;align-items:center;justify-content:center;text-align:center;font-family:"Alegreya Sans",sans-serif;font-weight:700;font-size:18px;line-height:20px;color:var(--navy)}
.card.featured .card-head{background:#fbe7e2;color:var(--accent)}
.card-photo{margin:22px auto 0;width:110px;height:150px;border-radius:12px;background:linear-gradient(135deg,#ffffff,#e1e4e8)}
.card-rule{margin:28px 18px 0;height:1px;background:var(--line)}
.card-name{text-align:center;margin-top:12px;font-size:17px;color:#555a62;font-family:"Alegreya Sans",sans-serif}
.card-price{text-align:center;margin-top:6px;font-size:13px;font-weight:700;color:var(--navy)}

/* testimonials */
.testimonials{left:0;top:2350px;width:1200px;height:383px;background:var(--navy-deep)}
.avatar-ring{left:231px;top:2474px;width:154px;height:154px;border-radius:50%;border:2px solid #4d72a0}
.avatar{left:243px;top:2486px;width:130px;height:130px;border-radius:50%;background:linear-gradient(160deg,#c7b8a8,#8c7a6a)}
.quote{left:427px;top:2518px;width:540px;font-size:13px;line-height:19px;color:#dfe7f1}

/* articles */
.article-photo{left:385px;top:2855px;width:584px;height:238px;background:linear-gradient(120deg,#b08870 0%,#d9c3b0 50%,#e9ddd0 100%)}

/* cta */
.cta{left:0;top:3217px;width:1200px;height:120px;background:var(--navy)}
.cta-text{left:154px;top:3260px;font-size:27px;color:var(--white)}

/* footer */
.footer{left:0;top:3337px;width:1200px;height:328px;background:var(--footer)}
.col-title{position:absolute;top:3395px;font-family:"Alegreya Sans",sans-serif;font-weight:500;font-size:17px;color:var(--ink)}
.foot-text{position:absolute;font-size:13px;color:#555a62;line-height:22px}
.links{position:absolute;top:3455px;font-size:13px;line-height:26px;color:#555a62}
.links .current{color:var(--accent)}
.social{position:absolute;left:154px;top:3574px;display:flex;gap:7px}
.social i{display:block;width:24px;height:24px;border-radius:50%;background:var(--navy)}
.email-field{left:763px;top:3505px;width:280px;height:32px;border-radius:16px;background:var(--white);font-size:11px;color:#9aa0a8;padding:9px 16px}
.bottom-bar{left:0;top:3664px;width:1200px;height:63px;background:var(--bar)}
.copyright{left:154px;top:3687px;font-size:12px;color:#c9ccd2}
.to-top{left:1022px;top:3682px;width:24px;height:24px;border-radius:50%;background:var(--accent)}
</style>
</head>
<body>

<section class="hero" aria-label="Hero">
  <div class="abs hero-product" role="img" aria-label="Photo of two white medical alert pendant devices with red cross buttons"></div>
  <p class="abs hero-kicker">Our Medical Alert Systems:</p>
  <h1 class="abs hero-title">The perfect fit for your<br>lifestyle</h1>
  <a class="btn btn-accent hero-cta">Choose Your Device</a>
  <div class="dots" style="left:154px;top:526px"><i></i><i></i><i></i></div>
</section>

<header class="site-header">
  <div class="brand"><span class="brand-dot"></span><span class="brand-name">Elder Harbor Circle</span></div>
  <p class="call"><b>Call Us:</b> 555-018-2046</p>
  <a class="btn btn-accent login">Login</a>
  <nav class="nav">
    <span class="active">Home</span><span>About Us</span><span>Products</span><span>How It Works</span><span>Testimonials</span><span>Blog</span><span>Contact Us</span>
  </nav>
</header>

<!-- How it works -->
<h2 class="abs" style="left:231px;top:648px;font-size:26px;color:var(--ink)">How It Works</h2>
<div class="rule" style="left:211px;top:713px;width:130px"></div>
<p class="lead" style="left:348px;top:702px;width:622px">There are many variations of passages of Lorem Ipsum available, but the majority have suffered alteration in some form, by injected...</p>
<div class="steps">
  <div class="step">
    <svg width="60" height="68" viewBox="0 0 60 68" fill="none" stroke-width="2.4" stroke-linecap="round" stroke-linejoin="round">
      <circle cx="22" cy="20" r="16" stroke="#e0482c"/><circle cx="22" cy="20" r="9" stroke="#e0482c"/>
      <path d="M22 20v26l-5-5c-3-3-8 1-5 5l12 14h22l5-16c1-4-1-6-4-6h-12v-2c0-3-4-3-4 0v-2c0-3-4-3-4 0V20c0-3-5-3-5 0" stroke="#123f74"/>
    </svg>
    Press Your Medical<br>Alert Button
  </div>
  <div class="step">
    <svg width="70" height="68" viewBox="0 0 70 68" fill="none" stroke="#123f74" stroke-width="2.4" stroke-linecap="round">
      <path d="M14 36v-6a21 21 0 0 1 42 0v6"/><rect x="8" y="32" width="10" height="18" rx="4"/><rect x="52" y="32" width="10" height="18" rx="4"/>
      <path d="M57 50c0 8-8 12-18 12"/><circle cx="35" cy="62" r="4" stroke="#e0482c"/><path d="M27 38c4 4 12 4 16 0" stroke="#e0482c"/>
    </svg>
    Speak With an<br>Emergency Operator
  </div>
  <div class="step">
    <svg width="78" height="68" viewBox="0 0 78 68" fill="none" stroke="#123f74" stroke-width="2.4" stroke-linejoin="round">
      <path d="M4 20h44v32H4zM48 30h14l10 12v10H48z"/><circle cx="18" cy="54" r="6" fill="#fff"/><circle cx="60" cy="54" r="6" fill="#fff"/>
      <path d="M26 26v16M18 34h16" stroke="#e0482c" stroke-width="3"/>
    </svg>
    Receive<br>Immediate Help
  </div>
</div>
<a class="btn btn-navy" style="left:305px;top:963px;width:112px;height:32px">Read More</a>

<!-- Video + About -->
<div class="abs grey-band"></div>
<div class="abs video" role="img" aria-label="Video still of an older woman jogging outdoors with mountains and forest behind"></div>
<svg class="abs play" width="66" height="66" viewBox="0 0 66 66" fill="none"><circle cx="33" cy="33" r="30" stroke="#fff" stroke-width="3"/><path d="M27 21l18 12-18 12z" fill="#fff"/></svg>

<h2 class="abs" style="left:231px;top:1436px;font-size:26px;color:var(--ink)">About Us</h2>
<div class="rule" style="left:211px;top:1501px;width:130px"></div>
<p class="lead" style="left:348px;top:1487px;width:622px;font-size:13px;line-height:20px">Contrary to popular belief, Lorem Ipsum is not simply random text. It has roots in a piece of classical Latin literature from 45 BC, making it over 2000 years old. Tobias Wrenfield, a Latin professor at Ashcombe College in Vermont, looked up one of the more obscure Latin words, consectetur, from a Lorem Ipsum passage, and going through the cites of the word in classical literature, discovered the undoubtable source There are many variations of passages of Lorem Ipsum...</p>
<a class="btn btn-accent" style="left:305px;top:1627px;width:132px;height:33px">Discover More</a>

<!-- Products -->
<h2 class="abs" style="left:231px;top:1778px;font-size:26px;color:var(--ink)">Our Products</h2>
<a class="btn btn-navy" style="left:855px;top:1781px;width:111px;height:32px">View All</a>
<div class="rule" style="left:211px;top:1843px;width:160px"></div>
<p class="lead" style="left:385px;top:1832px;width:585px">There are many variations of passages of Lorem Ipsum available, but the majority have suffered alteration in some form, by injected...</p>

<article class="card" style="left:231px">
  <div class="card-head">At Home<br>Help</div>
  <div class="card-photo" role="img" aria-label="Photo of a white in-home medical alert pendant"></div>
  <div class="card-rule"></div>
  <p class="card-name">In-Home Medical Alert</p><p class="card-price">From $19.95/mo</p>
</article>
<article class="card featured" style="left:489px;top:1910px;height:373px">
  <div class="card-head">On-the-go<br>Help</div>
  <div class="card-photo" role="img" aria-label="Photo of a white mobile medical alert device with lanyard"></div>
  <div class="card-rule"></div>
  <p class="card-name">In-Home Medical Alert</p><p class="card-price">From $19.95/mo</p>
</article>
<article class="card" style="left:745px">
  <div class="card-head">Automatic Fall<br>Detection</div>
  <div class="card-photo" role="img" aria-label="Photo of a white fall detection medical alert pendant"></div>
  <div class="card-rule"></div>
  <p class="card-name">In-Home Medical Alert</p><p class="card-price">From $19.95/mo</p>
</article>

<!-- Testimonials -->
<section class="abs testimonials" aria-label="Testimonials"></section>
<h2 class="abs" style="left:231px;top:2408px;font-size:27px;color:var(--white)">What Customers Are Saying</h2>
<div class="rule" style="left:211px;top:2459px;width:225px;background:#4d72a0"></div>
<a class="btn btn-accent" style="left:855px;top:2408px;width:111px;height:33px">View All</a>
<div class="abs avatar-ring"></div>
<div class="abs avatar" role="img" aria-label="Portrait photo of a smiling senior couple"></div>
<p class="abs" style="left:427px;top:2484px;font-size:14px;font-weight:700;color:var(--white)">M. Ellory.</p>
<p class="abs quote">There are many variations of passages of Lorem Ipsum available, but the majority have suffered alteration in some form, by injected. There are many variations of passages of Lorem Ipsum available, but the majority have suffered alteration in some form, by injected humour, or randomised...</p>
<svg class="abs" style="left:427px;top:2612px" width="90" height="16" viewBox="0 0 90 16">
  <g fill="#f0a030"><path id="s" d="M8 1l2.2 4.6 5 .6-3.7 3.4 1 5L8 12.2 3.5 14.6l1-5L.8 6.2l5-.6z"/><use href="#s" x="17"/><use href="#s" x="34"/></g>
  <path d="M59 1l2.2 4.6 5 .6-3.7 3.4 1 5L59 12.2 54.5 14.6l1-5-3.7-3.4 5-.6z" fill="none" stroke="#f0a030"/><path d="M59 1v11.2L54.5 14.6l1-5-3.7-3.4 5-.6z" fill="#f0a030"/>
  <path d="M76 1l2.2 4.6 5 .6-3.7 3.4 1 5L76 12.2 71.5 14.6l1-5-3.7-3.4 5-.6z" fill="none" stroke="#f0a030"/>
</svg>
<div class="dots light" style="left:440px;top:2662px"><i></i><i></i><i></i><i></i></div>

<!-- Articles -->
<h2 class="abs" style="left:231px;top:2790px;font-size:26px;color:var(--ink)">Recent Articles</h2>
<div class="rule" style="left:211px;top:2857px;width:160px"></div>
<div class="dots" style="left:932px;top:2806px"><i></i><i></i><i></i><i></i></div>
<div class="abs article-photo" role="img" aria-label="Photo of a caregiver assisting a smiling elderly woman at home"></div>
<p class="abs" style="left:385px;top:3114px;font-size:12px;color:var(--accent);font-weight:700">30 - October - 2017</p>
<p class="abs" style="left:385px;top:3134px;font-size:17px;color:var(--navy);border-bottom:1px solid var(--navy)">Contrary to popular belief, Lorem Ipsum</p>
<a class="btn btn-navy" style="left:855px;top:3120px;width:111px;height:31px">View All</a>

<!-- CTA -->
<section class="abs cta" aria-label="Free trial"></section>
<p class="abs cta-text heading">Try Mobile Help Risk Free for 30 Days!</p>
<a class="btn btn-accent" style="left:755px;top:3260px;width:132px;height:33px">Get Started</a>
<a class="btn btn-ghost" style="left:907px;top:3260px;width:136px;height:33px">Shop Online</a>

<!-- Footer -->
<footer class="abs footer"></footer>
<p class="col-title" style="left:154px">Contact Us</p>
<p class="col-title" style="left:460px">Quick Link</p>
<p class="col-title" style="left:763px">Newsletter</p>
<div class="rule" style="left:154px;top:3428px;width:889px;background:#d3d6db"></div>

<p class="foot-text" style="left:154px;top:3455px">Need Help?</p>
<p class="foot-text" style="left:154px;top:3484px;font-size:16px">Call Us: 555-018-2046</p>
<p class="foot-text" style="left:154px;top:3506px;font-size:12px">hello@elderharborcircle.com</p>
<p class="foot-text" style="left:154px;top:3540px">Connect with Us:</p>
<div class="social"><i></i><i></i><i></i><i></i><i></i></div>

<div class="links" style="left:460px"><span class="current">— Home</span><br>About Us<br>How It Works<br>Testimonials<br>Blog</div>
<div class="links" style="left:612px">FAQ<br>GPS Login<br>My Account<br>Contact Us</div>

<p class="foot-text" style="left:763px;top:3450px;width:290px;font-size:12px;line-height:18px">Receive email-only deals, special offers and product exclusives.</p>
<div class="abs email-field">Enter Your Email ...</div>
<a class="btn btn-accent" style="left:763px;top:3553px;width:98px;height:31px">
  <svg width="13" height="13" viewBox="0 0 14 14" style="margin-right:6px"><path d="M1 7l12-6-4 12-2-5z" fill="#fff"/></svg>Send</a>

<div class="abs bottom-bar"></div>
<p class="abs copyright">© 2017 Elder Harbor Circle. All Rights Reserved.</p>
<div class="abs to-top"><svg width="24" height="24" viewBox="0 0 24 24"><path d="M8 14l4-4 4 4" stroke="#fff" stroke-width="2" fill="none"/></svg></div>

</body>
</html>
```